Werbetafel für Immobilienverwaltung
Zielgruppe
Wir sind im Kern eine Immobilienverwaltung, daher richten wir uns an Eigentümer/Investoren/Kapitalanleger. Neben der Verwaltung welche auch durch Hausmeisterservice (Grünarbeiten usw.) erweitert werden kann, bieten wir die Gutachtenerstellung sowie den Vertrieb (Maklertätigkeit in Verkauf sowie Vermietung) an.
Ein großer Vorteil ist unsere Digitale Arbeitsweise (noch keine Selbstverständlichkeit in der Branche).
Aufgabenstellung
Ziel ist es, das Unternehmen unaufdringlich jedoch wirksam und informativ auf einer Werbetafel zu präsentieren.
Maße der Tafel, welche sich im ausgangsbereich eines großen Lebensmittelunternehmens befindet, ist B 320cm x H 120cm.
Die Kundschaft läuft in ca. 1m Entfernung an der Tafel vorbei, sie sollte also von nahem nicht zu überrumpelt wirken.
Unser Logo sowie Telefonnummer sollte iwie untergebracht werden.
Gern auch eigene Ideen umsetzen falls Ihr welche habt.

```html
<!DOCTYPE html>
<html lang="de">
<head>
<meta charset="utf-8">
<title>Elbkontor Immobilien – Werbetafel</title>
<link rel="stylesheet" href="https://fonts.googleapis.com/css2?family=Roboto:wght@700;900&display=swap">
<style>
  :root {
    --backdrop: #f2f2f2;
    --board: #ffffff;
    --brand-red: #922022;
    --text-grey: #979893;
    --strip-grey: #ececef;
    --white: #ffffff;
  }
  html, body {
    margin: 0;
    width: 1200px;
    height: 960px;
    overflow: hidden;
    background: var(--backdrop);
  }
  .billboard {
    position: absolute;
    left: 40px;
    top: 130px;
    width: 1120px;
    height: 700px;
    background: var(--board);
    box-shadow: 0 10px 30px rgba(0, 0, 0, 0.08);
    font-family: "Roboto", Arial, sans-serif;
  }
  .billboard svg { display: block; }
  .brand-name { font-weight: 700; fill: var(--brand-red); }
  .headline { font-weight: 900; }
  .headline--grey { fill: var(--text-grey); }
  .headline--white { fill: var(--white); }
  .cta { font-weight: 700; fill: var(--brand-red); }
  .phone { font-weight: 900; fill: var(--text-grey); }
</style>
</head>
<body>
  <div class="billboard">
    <svg width="1120" height="700" viewBox="0 0 1120 700" xmlns="http://www.w3.org/2000/svg">
      <g class="brand">
        <rect x="708" y="96" width="30" height="30" fill="var(--brand-red)"/>
        <text class="brand-name" x="750" y="126" font-size="40" textLength="325" lengthAdjust="spacingAndGlyphs">Elbkontor Immobilien</text>
      </g>

      <polygon class="band" points="0,384 1120,320 1120,426 0,491" fill="var(--brand-red)"/>
      <polygon class="strip" points="0,688 1120,624 1120,700 0,700" fill="var(--strip-grey)"/>

      <g transform="rotate(-3.3 124 362)">
        <text class="headline headline--grey" x="124" y="362" font-size="100" textLength="711" lengthAdjust="spacingAndGlyphs">Ihre Immobilie -</text>
      </g>
      <g transform="rotate(-3.3 131 460)">
        <text class="headline headline--white" x="131" y="460" font-size="100" textLength="807" lengthAdjust="spacingAndGlyphs">unser Know-Haus</text>
      </g>

      <g transform="rotate(-3.3 766 540)">
        <text class="cta" x="766" y="540" font-size="44" textLength="287" lengthAdjust="spacingAndGlyphs">Jen anmelden</text>
      </g>
      <g transform="rotate(-3.3 549 640)">
        <text class="phone" x="549" y="640" font-size="72" textLength="514" lengthAdjust="spacingAndGlyphs">0391 480 27 63</text>
      </g>
    </svg>
  </div>
</body>
</html>
```